Graphic to hang inside of fitness studio

This graphic will be printed on vinyl and hung inside of a boutique fitness studio for 2019. Graphic should read YEAR OF POSSIBILITIES.

2018 was called Year of Living Well. We would like something on trend for 2019 to hang within the studio as our 2019 Mantra. It is not a logo but for internal use. I've attached our logo here and the website is www.kestrelmovehall.com for additional reference. Thank you.

Target Market(s)

25 to 45 women

Industry/Entity Type

Fitness

Colors

Designer to choose colors to be used in the design.

Requirements
Must have
• On trend for 2019. (no people in image)
• Year of Possibilities in trendy font.
• Easy to read.
• Need text only.
• Do not need graphic images.
Nice to have
• Tintorell colours for 2019
• 2019 design trends for background
Should not have
• Male dominate colour or masculine traits.
• Photos of fitness.
• Photos of people.
• Photos of equipment.

```html
<!DOCTYPE html>
<html lang="en">
<head>
<meta charset="utf-8">
<title>2019 Year of Possibilities — Kestrel Move Hall</title>
<link rel="stylesheet" href="https://fonts.googleapis.com/css2?family=Oswald:wght@200;300;500;600&display=swap">
<style>
  :root {
    --teal: #3fb6a8;
    --teal-deep: #1f7f7a;
    --navy: #0d1e3a;
    --band-grey: #5a5a5c;
    --band-grey-dark: #3a3a3c;
    --white: #ffffff;
    --ink: #111214;
  }
  html, body {
    margin: 0;
    padding: 0;
    width: 849px;
    height: 1200px;
    overflow: hidden;
    background: var(--ink);
  }
  .poster {
    position: relative;
    width: 849px;
    height: 1200px;
    overflow: hidden;
    font-family: "Oswald", "Arial Narrow", sans-serif;
    background: var(--ink);
  }
  .photo-strength {
    position: absolute;
    inset: 0 0 auto 0;
    height: 880px;
    background:
      radial-gradient(ellipse 420px 300px at 420px 260px, #9a9a9a 0%, rgba(120,120,120,0) 70%),
      linear-gradient(170deg, #6e6e6e 0%, #4a4a4a 40%, #262626 75%, #1a1a1a 100%);
    clip-path: polygon(0 0, 849px 0, 849px 560px, 0 800px);
  }
  .photo-plank {
    position: absolute;
    left: 0;
    top: 640px;
    width: 849px;
    height: 560px;
    background:
      radial-gradient(ellipse 360px 200px at 520px 300px, rgba(63,182,168,0.85) 0%, rgba(63,182,168,0) 75%),
      linear-gradient(100deg, #6a1f5c 0%, #2b5e7a 45%, #1f8f88 65%, #0f2a4a 100%);
  }
  .brand {
    position: absolute;
    top: 92px;
    left: 632px;
    width: 168px;
    text-align: center;
  }
  .brand-name {
    margin: 0;
    font-weight: 500;
    font-size: 21px;
    letter-spacing: 0.5px;
    color: var(--teal);
    line-height: 1.2;
    white-space: nowrap;
  }
  .brand-rule {
    height: 1px;
    background: var(--white);
    margin: 8px 0 10px;
  }
  .brand-web {
    margin: 0;
    font-weight: 500;
    font-size: 12.5px;
    color: var(--white);
    white-space: nowrap;
  }
  .bands {
    position: absolute;
    inset: 0;
  }
  .mantra-year { font-weight: 200; fill: var(--white); }
  .mantra-lead { font-weight: 300; fill: var(--white); }
  .mantra-word { font-weight: 600; fill: var(--white); }
</style>
</head>
<body>
<main class="poster">
  <div class="photo-strength" role="img" aria-label="Black and white photo of a woman doing a dumbbell row in a studio class"></div>
  <div class="photo-plank" role="img" aria-label="Teal and magenta toned photo of a woman holding a low push-up on the studio floor"></div>

  <header class="brand">
    <p class="brand-name">KESTREL MOVE HALL</p>
    <div class="brand-rule"></div>
    <p class="brand-web">www.kestrelmovehall.com</p>
  </header>

  <svg class="bands" width="849" height="1200" viewBox="0 0 849 1200" aria-hidden="false">
    <defs>
      <linearGradient id="tealBand" x1="0" y1="0" x2="1" y2="0">
        <stop offset="0" stop-color="#2a9a90"/>
        <stop offset="1" stop-color="#46bdb0"/>
      </linearGradient>
      <linearGradient id="greyBand" x1="0" y1="0" x2="1" y2="0">
        <stop offset="0" stop-color="#4e4e50"/>
        <stop offset="1" stop-color="#6a6a6c"/>
      </linearGradient>
    </defs>
    <polygon class="band-year-shadow" points="0,850 310,762 310,790 0,880" fill="#0d1e3a"/>
    <polygon class="band-year" points="0,725 310,636 310,766 0,852" fill="url(#tealBand)"/>
    <polygon class="band-mantra-shadow" points="300,830 849,670 849,700 300,860" fill="#2a2a2c"/>
    <polygon class="band-mantra" points="300,662 849,500 849,672 300,832" fill="url(#greyBand)"/>

    <text class="mantra-year" x="160" y="790" font-size="122" text-anchor="middle"
          transform="rotate(-16 160 760)">2019</text>
    <text class="mantra-lead" x="322" y="640" font-size="62"
          transform="rotate(-16 322 640)">YEAR OF</text>
    <text class="mantra-word" x="330" y="790" font-size="126" textLength="480" lengthAdjust="spacingAndGlyphs"
          transform="rotate(-16 330 790)">POSSIBILITIES</text>
  </svg>
</main>
</body>
</html>
```